Business Card Needed for Crafter of Pottery, Jewelry and Artwork

Calling all designers in search of an artistic challenge.

I need a new business card design for my pottery, jewelry and artwork business, Woven Glass and Tide, based in Vancouver BC.

I would like a card that is bright and inviting and preferably incorporates my logo and a sample of photos of my work while having a clean fresh look. The following contact details would preferably be included on the card as well:
• Helena Pikeworth
• Designer
• Phone: 604.555.0172
• Email: Designer@WovenGlassandTide.example
• Website: www.WovenGlassandTide.example
• Blog: www.ShapingHillside.example

The logo is attached in two color schemes in both Vector and Source formats. On past cards I’ve also included photos of my work. By including photos of the work the pieces are showcased and it catches people’s eye and prompts them to pick up the card and look at it more closely. For example, if I leave a stack in a coffee shop I want people to be drawn to the card, to pick it up and get a sense of the my product lines. Please feel free to pull photos of my work directly off of my website. If you need photos with higher pixels please let me know and I’ll email them directly to you. The website background is bffbda (191, 251, 218). I would like the business cards to match the feel of the website for consistency but the cards do not need to use the exact same colors. My website and current business card are predominantly turquoise shades. The background uses stripes provided by the website template. I don’t know the exact colors of the stripes.

My current business card is attached to show the use of photos in a design. Please note that I am not thrilled with my own design and am looking for variations and completely new designs. This example is not meant to be used as a template or starting point.

Here is some background surrounding my company:
WGT offers one of a kind jewelry, pottery, artwork and leather bags each designed with a twist. The pottery varies from rustic every day functional ware to raku artwork. The jewelry ranges from simple sterling every day pieces to multimedia pieces incorporating stone, metal, ceramics and fabric. The artwork is multimedia, typically acrylic paired with a natural element such as bark. All the bags are leather with reworked kimono fabric or patterned silk lining.

Feel free to check out my website to get a flavour for my work and the color scheme I've used on marketing materials so far. www.wovenglassandtide.example
Updates

Thank you to everyone who has submitted a design so far. I hope everyone has received some helpful feedback.

I'm going to post a survey to customers and friends asking for their votes. If you have new designs to submit please try to get them in by Saturday March 30 at noon so that I can include it in the survey launch.

Thank you

Target Market(s)

Females aged 25-65 interested in one of a kind functional pottery and jewelry.

Industry/Entity Type

Coffee Shop

Requirements
Must have
• Contact information, website, blog
Nice to have
• Logo, photos

```html
<!DOCTYPE html>
<html lang="en">
<head>
<meta charset="utf-8">
<title>Woven Glass and Tide – Business Card Designs</title>
<link rel="stylesheet" href="https://fonts.googleapis.com/css2?family=Cormorant+Garamond:wght@500&family=Niconne&display=swap">
<style>
  :root {
    --teal: #0cb5ad;
    --teal-deep: #0a9e97;
    --teal-pale: #b9e3df;
    --white: #ffffff;
    --ink: #222222;
    --grey: #666666;
    --label: #555555;
    --page: #ffffff;
  }
  * { margin: 0; padding: 0; box-sizing: border-box; }
  html, body {
    width: 1200px; height: 859px; overflow: hidden;
    background: var(--page);
  }
  .sheet { position: relative; width: 1200px; height: 859px; }

  .caption {
    position: absolute; width: 300px; text-align: center;
    font-family: "Niconne", cursive; font-size: 22px; color: var(--label);
  }
  .caption--front { top: 6px; }
  .caption--back { top: 818px; }
  .caption--left { left: 148px; }
  .caption--right { left: 754px; }

  .card { position: absolute; overflow: hidden; }
  .card--front-left { left: 1px; top: 52px; width: 594px; height: 372px; background: var(--teal); }
  .card--front-right { left: 607px; top: 52px; width: 593px; height: 372px; background: var(--teal); }
  .card--back-left { left: 1px; top: 435px; width: 594px; height: 372px; background: var(--white); border: 1px solid var(--teal); }
  .card--back-right { left: 607px; top: 435px; width: 593px; height: 372px; background: var(--teal); }

  .wordmark {
    position: absolute; left: 0; width: 100%; text-align: center;
    font-family: "Cormorant Garamond", serif; font-weight: 500;
    color: var(--white); text-transform: uppercase;
    letter-spacing: 6px; font-size: 42px; line-height: 1.15;
  }
  .card--front-left .wordmark { top: 150px; }
  .card--front-right .wordmark { top: 118px; }

  .photo-band {
    position: absolute; left: 0; top: 256px; width: 100%; height: 88px;
    border-top: 3px solid var(--teal-deep); border-bottom: 3px solid var(--teal-deep);
  }
  .photo-band__fill {
    width: 100%; height: 100%;
    background: linear-gradient(90deg, #3a3a3a 0%, #c9c4b8 17%, #3a3a3a 34%, #cfcabc 50%, #3a3a3a 67%, #cbc6b9 84%, #3a3a3a 100%);
  }

  .contact-name {
    position: absolute; left: 22px; top: 20px;
    font-family: "Niconne", cursive; font-size: 19px; line-height: 1.3;
  }
  .contact-name__name { color: var(--teal); font-weight: 700; }
  .contact-name__role { color: var(--ink); font-weight: 700; }
  .card--back-right .contact-name__name,
  .card--back-right .contact-name__role { color: var(--white); }

  .contact-list {
    position: absolute; left: 22px; top: 242px; list-style: none;
    font-family: "Niconne", cursive; font-size: 17px; line-height: 27.5px;
  }
  .contact-list__label { color: var(--teal); font-weight: 700; }
  .contact-list__value { color: var(--grey); }
  .card--back-right .contact-list__label,
  .card--back-right .contact-list__value { color: var(--white); }

  .collage {
    position: absolute; left: 185px; top: 36px; width: 385px; height: 180px;
    border-radius: 6px;
    background: linear-gradient(120deg, #d89a3c 0%, #e9e4dc 35%, #c7a55a 60%, #b76a2a 100%);
    opacity: .85;
  }
  .footer-bar {
    position: absolute; left: 0; bottom: 0; width: 100%; height: 8px;
    background: var(--teal);
  }

  .showcase { position: absolute; right: 0; top: 0; }
  .showcase__art {
    position: absolute; left: 383px; top: 28px; width: 172px; height: 156px;
    border-radius: 14px;
    background: radial-gradient(circle at 50% 55%, #2a2f8a 0%, #2a3590 55%, #5fb8df 100%);
  }
</style>
</head>
<body>
<main class="sheet">
  <p class="caption caption--front caption--left">Front Design</p>
  <p class="caption caption--front caption--right">Front Design</p>

  <section class="card card--front-left" aria-label="Front design, plain">
    <h1 class="wordmark">Woven Glass<br>and Tide</h1>
  </section>

  <section class="card card--front-right" aria-label="Front design with photo band">
    <h1 class="wordmark">Woven Glass<br>and Tide</h1>
    <div class="photo-band">
      <div class="photo-band__fill" role="img" aria-label="Row of jewellery photos: necklaces and bangles"></div>
    </div>
  </section>

  <section class="card card--back-left" aria-label="Back design, white">
    <div class="contact-name">
      <div class="contact-name__name">Helena Pikeworth</div>
      <div class="contact-name__role">Designer</div>
    </div>
    <div class="collage" role="img" aria-label="Scattered photos of the designer, bangles and past cards"></div>
    <ul class="contact-list">
      <li><span class="contact-list__label">Phone:</span> <span class="contact-list__value">604.555.0172</span></li>
      <li><span class="contact-list__label">Email:</span> <span class="contact-list__value">Designer@WovenGlassandTide.example</span></li>
      <li><span class="contact-list__label">Website:</span> <span class="contact-list__value">www.WovenGlassandTide.example</span></li>
      <li><span class="contact-list__label">Blog:</span> <span class="contact-list__value">www.ShapingHillside.example</span></li>
    </ul>
    <div class="footer-bar"></div>
  </section>

  <section class="card card--back-right" aria-label="Back design, turquoise">
    <svg class="showcase" width="593" height="230" viewBox="0 0 593 230" aria-hidden="true">
      <path d="M330 0 L364 178 Q372 222 416 224 L593 224 L593 0 Z" fill="var(--teal-pale)"/>
      <path d="M328 0 L360 170 Q368 214 412 216 L593 216 L593 0 Z" fill="var(--white)"/>
    </svg>
    <div class="showcase__art" role="img" aria-label="Illustration of pottery vessels"></div>
    <div class="contact-name">
      <div class="contact-name__name">Helena Pikeworth</div>
      <div class="contact-name__role">Designer</div>
    </div>
    <ul class="contact-list">
      <li><span class="contact-list__label">Phone:</span> <span class="contact-list__value">604.555.0172</span></li>
      <li><span class="contact-list__label">Email:</span> <span class="contact-list__value">Designer@WovenGlassandTide.example</span></li>
      <li><span class="contact-list__label">Website:</span> <span class="contact-list__value">www.WovenGlassandTide.example</span></li>
      <li><span class="contact-list__label">Blog:</span> <span class="contact-list__value">www.ShapingHillside.example</span></li>
    </ul>
  </section>

  <p class="caption caption--back caption--left">Back Design</p>
  <p class="caption caption--back caption--right">Back Design</p>
</main>
</body>
</html>
```